Welland Dental, P.C. New stationary and business card for modern Dental Office

We need a new stationary/envelope/business card design using our newly designed logo. We are looking for an upscale look. Our new logo is used on our signage, using black as the background and white for the lettering. We would like the stationary to have black, white, possible greys or silver. We are looking for a letterhead, envelope, and business card design for three different employees, as well as a 4th card, same design, but just general with no employee name.
Updates

Project Deadline Extended
Reason: We began this project in the middle of our move into our new office. Things got pretty hectic and we just didn't have the time to go through designs. We now settled in and finally eliminated the designs that didn't work for us. We would like to extend the project another 5 days, and then finalize our decision. Most of the submissions showed business cards alone, with no stationary designs. Our original request was for stationary and business cards. Please keep this in mind.

Target Market(s)

Dental patients expecting high quality, cosmetic dentistry

Industry/Entity Type

Business

Contact Information for Business Card

Will need a design using our logo. All cards will be the same, other than that one card will have Office Managers name, One for the Doctor, Hygienist,
1. Office Manager - Marisol Penrose
2. Hygienist - Courtney Whitlock
3. Owen T. Welland, D.D.S.
4. One general one with no staff names

Font styles to use
Other font styles liked:
• see upload

Colors
000000
1b1b1b
757575
c9c9c9
e8e8e8
ffffff

Requirements
Must have
• -Logo
• -Phone number (718)555-0143
• -Address: 4392 63rd Ave
• Lower Level
• Brooklyn, NY 11398

```html
<!DOCTYPE html>
<html lang="en">
<head>
<meta charset="utf-8">
<title>Welland Dental, P.C. — Stationery Set</title>
<link href="https://fonts.googleapis.com/css2?family=Open+Sans:wght@400;600;700&display=swap" rel="stylesheet">
<style>
  :root{
    --black:#000000;
    --ink:#1b1b1b;
    --grey:#757575;
    --silver:#c9c9c9;
    --mist:#e8e8e8;
    --white:#ffffff;
    --backdrop:#eeeeee;
  }
  *{box-sizing:border-box;margin:0;padding:0}
  html,body{width:945px;height:1200px;overflow:hidden}
  body{background:var(--backdrop);font-family:"Open Sans",Arial,sans-serif;color:var(--ink);position:relative}

  .sheet{position:absolute;overflow:hidden;box-shadow:0 2px 8px rgba(0,0,0,.12)}
  .sheet--light{background:var(--white)}
  .sheet--dark{background:radial-gradient(circle at 55% 45%, #262626 0%, var(--ink) 45%, var(--black) 100%)}

  .swoosh{position:absolute;right:0;bottom:0;width:100%;height:100%;display:block}

  .brand{position:absolute;display:flex;align-items:center;gap:.45em;font-weight:600;white-space:nowrap;letter-spacing:.01em}
  .brand__dot{width:1.1em;height:1.1em;border-radius:50%;border:.12em solid currentColor;flex:none}
  .brand--light{color:var(--white)}
  .brand--muted{color:var(--grey)}

  .tab{position:absolute;left:0;background:var(--black)}

  /* letterhead */
  .letterhead{left:40px;top:40px;width:300px;height:424px}
  .letterhead .brand{top:22px;right:22px;font-size:11px}
  .letter-body{position:absolute;left:26px;top:64px;width:248px;font-size:5.4px;line-height:1.55;color:var(--ink)}
  .letter-body p{margin-bottom:6px}
  .letter-footer{position:absolute;left:0;top:316px;display:flex;align-items:flex-start;font-size:5.2px}
  .letter-footer .tab{position:relative;width:6px;height:18px;margin-right:10px}
  .letter-footer__name{font-weight:700;font-size:6px}
  .letter-footer__role{color:var(--grey)}
  .letter-footer__rule{width:1px;height:18px;background:var(--silver);margin:0 8px}
  .letter-footer__contact{line-height:1.6;color:var(--ink)}

  /* presentation folder */
  .folder{left:370px;top:40px;width:300px;height:424px}
  .folder .brand{left:50%;top:50%;transform:translate(-50%,-50%);font-size:17px}

  /* small cards */
  .mini-back{left:700px;top:40px;width:205px;height:117px}
  .mini-back .brand{left:50%;top:50%;transform:translate(-50%,-50%);font-size:11.5px}
  .mini-front{left:700px;top:177px;width:205px;height:117px}
  .mini-front .brand{top:10px;right:10px;font-size:7.5px}
  .mini-front .tab{top:28px;width:4px;height:18px}
  .mini-front__name{position:absolute;left:16px;top:28px;font-size:7.5px;font-weight:700}
  .mini-front__role{position:absolute;left:16px;top:39px;font-size:5.5px;color:var(--grey)}
  .mini-front__contact{position:absolute;left:16px;bottom:12px;font-size:5.5px;line-height:1.6}

  /* envelope */
  .envelope{left:40px;top:500px;width:560px;height:270px}
  .envelope .brand{top:22px;left:26px;font-size:14px}
  .envelope__return{position:absolute;left:26px;top:52px;font-size:7.5px;color:var(--ink);letter-spacing:.02em}

  /* business cards, full size */
  .card{top:840px;width:420px;height:240px}
  .card--back{left:40px}
  .card--back .brand{left:50%;top:50%;transform:translate(-50%,-50%);font-size:22px}
  .card--front{left:485px}
  .card--front .brand{top:22px;right:22px;font-size:14px}
  .card--front .tab{top:56px;width:8px;height:34px}
  .card__name{position:absolute;left:26px;top:56px;font-size:15px;font-weight:700;color:var(--ink)}
  .card__role{position:absolute;left:26px;top:77px;font-size:10px;color:var(--silver)}
  .card__contact{position:absolute;left:26px;bottom:26px;font-size:11.5px;line-height:1.45;letter-spacing:.02em;list-style:none}
  .card__contact li{display:flex;align-items:flex-start;gap:8px;margin-top:5px}
  .card__contact svg{width:10px;height:12px;margin-top:2px;flex:none;fill:var(--silver)}
</style>
</head>
<body>

<!-- Letterhead -->
<section class="sheet sheet--light letterhead" aria-label="Letterhead">
  <div class="brand brand--muted"><span>Welland Dental, P.C.</span><span class="brand__dot"></span></div>
  <div class="letter-body">
    <p>Dear Patient,</p>
    <p>Thank you for choosing our practice for your dental care. We are pleased to welcome you and your family, and we look forward to helping you keep a healthy, confident smile for many years.</p>
    <p>Our team offers general and cosmetic treatment in a calm, modern office. Every visit begins with a careful exam and a clear plan, so you always know what to expect.</p>
    <p>Please arrive ten minutes before your appointment and bring your insurance card. If you need to change a visit, call our front desk at least one day ahead.</p>
    <p>We value your trust and look forward to seeing you soon.</p>
    <p>Sincerely,</p>
  </div>
  <div class="letter-footer">
    <span class="tab"></span>
    <div><div class="letter-footer__name">Dr. Owen T. Welland</div><div class="letter-footer__role">Dentist</div></div>
    <span class="letter-footer__rule"></span>
    <div class="letter-footer__contact">4392 63rd Ave Lower Level, Brooklyn, NY 11398<br>(718) 555-0143</div>
  </div>
  <svg class="swoosh" viewBox="0 0 100 100" preserveAspectRatio="none" aria-hidden="true">
    <path d="M38,100 Q82,93 100,68 L100,100 Z" fill="var(--silver)"/>
    <path d="M46,100 Q86,95 100,73 L100,100 Z" fill="var(--black)"/>
  </svg>
</section>

<!-- Presentation folder -->
<section class="sheet sheet--dark folder" aria-label="Presentation folder">
  <div class="brand brand--light"><span>Welland Dental, P.C.</span><span class="brand__dot"></span></div>
</section>

<!-- Small business card, back -->
<section class="sheet sheet--dark mini-back" aria-label="Business card back">
  <div class="brand brand--light"><span>Welland Dental, P.C.</span><span class="brand__dot"></span></div>
</section>

<!-- Small business card, front -->
<section class="sheet sheet--light mini-front" aria-label="Business card front">
  <svg class="swoosh" viewBox="0 0 100 100" preserveAspectRatio="none" aria-hidden="true">
    <path d="M40,100 Q82,90 100,30 L100,100 Z" fill="var(--silver)"/>
    <path d="M49,100 Q86,92 100,40 L100,100 Z" fill="var(--black)"/>
  </svg>
  <div class="brand brand--muted"><span>Welland Dental, P.C.</span><span class="brand__dot"></span></div>
  <span class="tab"></span>
  <div class="mini-front__name">Dr. Owen T. Welland</div>
  <div class="mini-front__role">Dentist</div>
  <div class="mini-front__contact">4392 63rd Ave Lower Level,<br>Brooklyn, NY 11398<br>(718) 555-0143</div>
</section>

<!-- Envelope -->
<section class="sheet sheet--light envelope" aria-label="Envelope">
  <div class="brand brand--muted"><span>Welland Dental, P.C.</span><span class="brand__dot"></span></div>
  <div class="envelope__return">If undelivered, please return to: 4392 63RD AVE LOWER LEVEL, BROOKLYN, NY 11398</div>
  <svg class="swoosh" viewBox="0 0 100 100" preserveAspectRatio="none" aria-hidden="true">
    <path d="M50,100 Q84,86 100,45 L100,100 Z" fill="var(--silver)"/>
    <path d="M57,100 Q88,89 100,55 L100,100 Z" fill="var(--black)"/>
  </svg>
</section>

<!-- Business card, back -->
<section class="sheet sheet--dark card card--back" aria-label="Business card back">
  <div class="brand brand--light"><span>Welland Dental, P.C.</span><span class="brand__dot"></span></div>
</section>

<!-- Business card, front -->
<section class="sheet sheet--light card card--front" aria-label="Business card front">
  <svg class="swoosh" viewBox="0 0 100 100" preserveAspectRatio="none" aria-hidden="true">
    <path d="M40,100 Q82,90 100,30 L100,100 Z" fill="var(--silver)"/>
    <path d="M49,100 Q86,92 100,40 L100,100 Z" fill="var(--black)"/>
  </svg>
  <div class="brand brand--muted"><span>Welland Dental, P.C.</span><span class="brand__dot"></span></div>
  <span class="tab"></span>
  <div class="card__name">Dr. Owen T. Welland</div>
  <div class="card__role">Dentist</div>
  <ul class="card__contact">
    <li>
      <svg viewBox="0 0 10 12" aria-hidden="true"><path d="M5 0a4 4 0 0 0-4 4c0 3 4 8 4 8s4-5 4-8a4 4 0 0 0-4-4zm0 5.6A1.6 1.6 0 1 1 5 2.4a1.6 1.6 0 0 1 0 3.2z"/></svg>
      <span>4392 63RD AVE LOWER LEVEL,<br>BROOKLYN, NY 11398</span>
    </li>
    <li>
      <svg viewBox="0 0 10 12" aria-hidden="true"><path d="M2.2 1.5 3.6 1l1.2 2.6-1 .8c.5 1.4 1.3 2.6 2.4 3.4l1-.7 2 1.8-.8 1.4C5.3 10 1.6 5.7 2.2 1.5z"/></svg>
      <span>(718) 555-0143</span>
    </li>
  </ul>
</section>

</body>
</html>
```